Brass Kite Gig - 20 Years of Funk

I'm with a funk band called Brass Kite. We are celebrating our 20 year anniversary with a show on August 3, 2024. We would like some banners made for social media to help promote the gig. I'm attaching some examples of our 10 year anniversary gig so you can at least get an idea of what we are looking for.

Here's the text for the banners:
BRASS KITE Anniversary Gig - 20 Years of Funk!
Saturday, August 10, 2024
with special guest: Marco Delvin
Doors at 7pm, Show at 8pm

We would like three sizes:
1920 x 1005 pixels
1080 x 1080 pixels
1080 x 1920 pixels

You can check out our website for more ideas of our graphic style, etc.. www.brasskiteband.example

```html
<!DOCTYPE html>
<html lang="en">
<head>
<meta charset="utf-8">
<title>Brass Kite – 20 Years of Funk Banner</title>
<link rel="stylesheet" href="https://fonts.googleapis.com/css2?family=Oswald:wght@400;500;600;700&family=Archivo:wght@700&display=swap">
<style>
  :root {
    --page: #e9e9e9;
    --ink: #0b0b0b;
    --lime: #c6e81c;
    --white: #ffffff;
    --silver-hi: #f4f4f4;
    --silver-lo: #9a9a9a;
    --photo-dark: #1a1a1a;
    --photo-mid: #4a4a4a;
  }
  * { box-sizing: border-box; margin: 0; padding: 0; }
  html, body { width: 1200px; height: 1096px; overflow: hidden; background: var(--page); }
  .banner {
    position: absolute; left: 40px; top: 255px;
    width: 1120px; height: 586px;
    background: var(--ink); overflow: hidden;
    font-family: "Oswald", sans-serif; color: var(--white);
    box-shadow: 0 20px 40px rgba(0,0,0,.25);
  }
  .band-photo {
    position: absolute; left: 0; top: 0; width: 100%; height: 390px;
    background: linear-gradient(180deg, var(--photo-dark) 0%, var(--photo-mid) 55%, #2a2a2a 100%);
  }
  .photo-fade {
    position: absolute; left: 0; top: 0; width: 100%; height: 390px;
    background: linear-gradient(90deg, rgba(0,0,0,.55) 0%, rgba(0,0,0,0) 30%, rgba(0,0,0,0) 70%, rgba(0,0,0,.55) 100%);
  }
  .spotlight {
    position: absolute; left: 418px; top: 110px; width: 290px; height: 290px;
    border-radius: 50%; background: var(--lime);
  }
  .singer-photo {
    position: absolute; left: 450px; top: 40px; width: 230px; height: 350px;
    border-radius: 110px 110px 0 0;
    background: linear-gradient(180deg, #5a5a5a 0%, #3a3a3a 60%, #2b2b2b 100%);
  }
  .torn-band { position: absolute; left: 0; top: 358px; width: 1120px; height: 70px; }
  .date { position: absolute; left: 52px; top: 30px; text-align: center; line-height: 1; }
  .date .day { font-size: 38px; font-weight: 600; }
  .date .month { font-size: 46px; font-weight: 700; color: var(--lime); margin-top: 4px; }
  .date .num { font-size: 84px; font-weight: 700; margin-top: 2px; }
  .date .num sup { font-size: 44px; vertical-align: 28px; }
  .date .year {
    display: block; margin-top: 6px; background: var(--lime); color: var(--ink);
    font-family: "Archivo", sans-serif; font-size: 22px; letter-spacing: 4px;
    padding: 4px 0; width: 190px;
  }
  .times {
    position: absolute; right: 42px; top: 110px; width: 118px;
    border: 3px solid var(--white); padding: 8px 6px; text-align: center; line-height: 1;
  }
  .times .label { font-size: 17px; color: var(--lime); font-weight: 500; }
  .times .hour { font-size: 40px; font-weight: 700; margin: 2px 0 6px; }
  .times .hour:last-child { margin-bottom: 0; }
  .sparks { position: absolute; right: 44px; top: 300px; width: 14px; }
  .sparks span { display: block; font-size: 16px; line-height: 22px; text-align: center; }
  .headline { position: absolute; left: 0; width: 100%; text-align: center; }
  .tagline {
    top: 388px; left: 50%; width: auto; transform: translateX(-50%);
    background: var(--ink); border: 2px solid var(--white);
    font-size: 22px; letter-spacing: 6px; padding: 2px 14px; font-weight: 500;
  }
  .title {
    top: 420px; font-size: 84px; font-weight: 700; line-height: 1.05;
    background: linear-gradient(180deg, var(--silver-hi) 0%, #c9c9c9 50%, var(--silver-lo) 100%);
    -webkit-background-clip: text; background-clip: text; color: transparent;
  }
  .band-name { top: 506px; font-size: 58px; font-weight: 700; color: var(--lime); line-height: 1; }
  .guest { position: absolute; left: 58px; top: 440px; font-size: 30px; line-height: 1.08; letter-spacing: 2px; }
  .guest .label { color: var(--lime); font-weight: 400; }
  .guest .name { font-weight: 700; }
  .site { position: absolute; right: 42px; top: 522px; font-size: 13px; letter-spacing: 3px; font-weight: 500; }
</style>
</head>
<body>
  <main class="banner">
    <div class="band-photo" role="img" aria-label="Black and white photo of the band standing among palm trees"></div>
    <div class="photo-fade"></div>
    <div class="spotlight"></div>
    <div class="singer-photo" role="img" aria-label="Black and white photo of the lead singer in a white hat singing into a microphone"></div>

    <svg class="torn-band" viewBox="0 0 1120 70" preserveAspectRatio="none" aria-hidden="true">
      <path fill="#c6e81c" d="M0 14 L60 10 L120 16 L200 8 L280 14 L360 6 L440 12 L520 6 L600 10 L700 4 L780 12 L860 6 L940 14 L1020 6 L1120 10 L1120 26 L1040 22 L960 30 L880 22 L800 28 L720 20 L620 26 L520 20 L420 28 L320 22 L220 30 L140 22 L60 28 L0 24 Z"/>
      <path fill="#0b0b0b" d="M0 24 L60 28 L140 22 L220 30 L320 22 L420 28 L520 20 L620 26 L720 20 L800 28 L880 22 L960 30 L1040 22 L1120 26 L1120 70 L0 70 Z"/>
    </svg>

    <div class="date">
      <div class="day">SATURDAY</div>
      <div class="month">AUGUST</div>
      <div class="num">10<sup>th</sup></div>
      <span class="year">2024</span>
    </div>

    <div class="times">
      <div class="label">DOORS AT</div>
      <div class="hour">7PM</div>
      <div class="label">SHOW AT</div>
      <div class="hour">8PM</div>
    </div>

    <div class="sparks" aria-hidden="true"><span>+</span><span>+</span><span>+</span></div>

    <div class="headline tagline">ANNIVERSARY GIG</div>
    <div class="headline title">20 YEARS OF FUNK!</div>
    <div class="headline band-name">Brass Kite</div>

    <div class="guest">
      <div class="label">SPECIAL<br>GUEST:</div>
      <div class="name">MARCO<br>DELVIN</div>
    </div>

    <div class="site">WWW.BRASSKITEBAND.EXAMPLE</div>
  </main>
</body>
</html>
```